Medical Clinic Group Looking for Website Design

We own and operate medical clinics and are looking looking to revamp our website. Our current website is www.brightwaycareclinics.ca We need our website to be more functional, user friendly, and easier to maintain.

```html
<!DOCTYPE html>
<html lang="en">
<head>
<meta charset="utf-8">
<title>Brightway Care Clinics</title>
<link href="https://fonts.googleapis.com/css2?family=Montserrat:wght@400;500;600&family=Questrial&display=swap" rel="stylesheet">
<style>
:root{
  --teal:#33c6d3;
  --teal-dark:#23a9b6;
  --ice:#c9f2f5;
  --mist:#ecfbfc;
  --grey:#7d7d7f;
  --ink:#1b1b1b;
  --text:#4a4a4a;
  --footer:#171717;
  --white:#ffffff;
}
*{box-sizing:border-box;margin:0;padding:0}
html,body{width:1200px;height:3601px;overflow:hidden}
body{position:relative;font-family:"Montserrat",sans-serif;color:var(--text);background:var(--white)}
.abs{position:absolute}
.display{font-family:"Questrial",sans-serif;font-weight:400}
.center{text-align:center}

/* header */
.site-header{left:0;top:0;width:1200px;height:98px;background:var(--white)}
.brand{display:flex;align-items:center;gap:14px}
.brand-mark{width:46px;height:46px;border-radius:50%;background:var(--teal)}
.brand-name{font-family:"Montserrat",sans-serif;font-weight:500;font-size:34px;color:var(--teal);letter-spacing:.5px}
.top-btn{top:0;height:38px;background:var(--teal);color:var(--white);font-size:13px;display:flex;align-items:center;justify-content:center;gap:8px;border-radius:0 0 6px 6px}
.main-nav{top:48px;left:595px;width:605px;border-top:1px solid #e3e3e3;display:flex;justify-content:space-around;padding:14px 0 0;font-size:13px;color:#333}

/* hero */
.hero{left:0;top:98px;width:1200px;height:600px;overflow:hidden}
.hero-photo{width:100%;height:100%;background:linear-gradient(110deg,#c9c6c1 0%,#e7e4df 35%,#8da6b8 60%,#d6d6d6 100%)}
.hero-card{left:40px;top:42px}
.hero-text{left:110px;top:198px;width:420px}
.kicker{font-size:11px;color:var(--teal);letter-spacing:.1px}
.hero-title{font-size:50px;line-height:56px;color:var(--ink);margin-top:14px}
.hero-copy{font-size:12.5px;line-height:22px;color:#333;margin-top:14px;padding:0 14px}
.btn{display:inline-block;background:var(--teal);color:var(--white);font-size:14px;border-radius:4px}
.dots{left:1136px;top:352px}
.dot{width:10px;height:10px;border-radius:50%;background:var(--white);margin-bottom:19px}
.dot.on{background:var(--teal)}

/* welcome */
.welcome{left:0;top:698px;width:1200px;height:519px}
.welcome-panel{left:0;top:0;width:245px;height:519px;background:var(--mist)}
.quick-item{left:0;width:365px;height:60px}
.quick-bar{left:0;top:0;width:310px;height:60px;background:var(--teal);color:var(--white);font-size:17px;font-weight:500;display:flex;align-items:center;padding-left:32px;border-radius:0 30px 30px 0}
.quick-icon{left:300px;top:-3px;width:66px;height:66px}
.welcome-copy{left:404px;top:96px;width:355px}
.eyebrow{font-size:16px;color:var(--ink);font-weight:500}
.section-title{font-size:36px;color:var(--teal);line-height:46px}
.body-copy{font-size:12px;line-height:21px;color:#444}
.doctors{left:778px;top:182px;width:372px;height:337px;background:linear-gradient(180deg,#f1f4f6,#dde7ef);border-radius:8px 8px 0 0}

/* services */
.services{left:0;top:1217px;width:1200px;height:616px;background:var(--ice)}
.service{width:330px}
.service-photo{width:300px;height:300px;border-radius:50%;margin:0 auto;border:4px solid var(--grey)}
.service-photo.feature{border-color:var(--teal)}
.service h3{font-size:17px;font-weight:500;color:var(--ink);margin-top:20px}
.service p{font-size:12.5px;line-height:21px;margin-top:8px;padding:0 10px}

/* testimonials */
.testimonials{left:0;top:1833px;width:1200px;height:454px}
.quote{left:308px;top:162px;width:584px;font-size:12.8px;line-height:21px;color:#444}
.author{font-size:18px;color:var(--teal);letter-spacing:.5px}

/* news */
.news{left:0;top:2287px;width:1200px;height:597px;background:var(--mist)}
.news-card{top:147px;width:340px}
.news-photo{width:340px;height:225px;border-radius:8px}
.news-meta{left:24px;top:207px;height:40px;width:225px;background:var(--teal);color:var(--white);font-size:13px;display:flex;align-items:center;gap:10px;padding:0 18px;border-radius:6px 6px 0 0}
.news-card h4{font-size:20px;font-weight:500;line-height:30px;color:var(--ink);margin-top:27px}
.news-card p{font-size:12.5px;line-height:21px;margin-top:8px}
.learn{font-size:16px;color:var(--teal);margin-top:12px;display:flex;align-items:center;gap:6px}

/* cta */
.cta{left:0;top:2884px;width:1200px;height:361px;background:linear-gradient(100deg,#2cb2be 0%,#3ec3ce 50%,#2aaab6 100%);color:var(--white)}
.cta .eyebrow{color:#123}
.cta-title{font-size:38px;line-height:46px;color:var(--white)}
.cta-btn{background:var(--white);color:#333;font-size:13px;border-radius:4px}

/* footer */
.site-footer{left:0;top:3245px;width:1200px;height:321px;background:var(--footer);color:#ddd}
.foot-head{font-size:16px;color:var(--teal);font-weight:500}
.foot-list{list-style:none;font-size:12.5px}
.foot-list li{margin-bottom:14px;display:flex;align-items:center;gap:16px}
.foot-list li::before{content:"";width:4px;height:4px;border-radius:50%;background:var(--teal)}
.social{width:30px;height:30px;border-radius:50%;border:1.5px solid #ddd}
.social.on{background:var(--teal);border-color:var(--teal)}
.copyright{left:0;top:3566px;width:1200px;height:35px;background:var(--teal);color:var(--white);font-size:12px;display:flex;align-items:center;justify-content:center}
</style>
</head>
<body>

<header class="site-header abs">
  <div class="brand abs" style="left:60px;top:22px">
    <span class="brand-mark"></span>
    <span class="brand-name">brightway</span>
  </div>
  <a class="top-btn abs" style="left:755px;width:196px">Book An Appointment</a>
  <a class="top-btn abs" style="left:968px;width:172px">
    <svg width="14" height="14" viewBox="0 0 24 24"><path fill="#fff" d="M6.6 10.8a15 15 0 006.6 6.6l2.2-2.2a1 1 0 011-.25 11.4 11.4 0 003.6.57 1 1 0 011 1V20a1 1 0 01-1 1A17 17 0 013 4a1 1 0 011-1h3.5a1 1 0 011 1 11.4 11.4 0 00.57 3.6 1 1 0 01-.25 1z"/></svg>
    +1 604-555-0148</a>
  <nav class="main-nav abs"><span>Locations</span><span>For Patients</span><span>For Providers</span><span>About Us</span><span>Book Online</span></nav>
</header>

<section class="hero abs">
  <div class="hero-photo" role="img" aria-label="Photo of a physiotherapist examining a teenage patient's knee in a bright clinic room"></div>
  <svg class="hero-card abs" width="560" height="560" viewBox="0 0 560 560">
    <rect x="80" y="80" width="400" height="400" rx="50" transform="rotate(45 280 280)" fill="#e9f9fa" stroke="#7d7d7f" stroke-width="22"/>
  </svg>
  <div class="hero-text abs center">
    <p class="kicker">WE'RE RENOVATING TO SERVE YOU BETTER</p>
    <h1 class="hero-title display">Exciting Things<br>Are Happening!</h1>
    <p class="hero-copy">Renovations have begun at our Riverside location! Over the next several months, we will be renovating the entire clinic to serve our existing patients better.</p>
  </div>
  <a class="btn abs center" style="left:265px;top:439px;width:109px;height:33px;line-height:33px">Book Now</a>
  <div class="dots abs"><div class="dot"></div><div class="dot on"></div><div class="dot"></div></div>
</section>

<section class="welcome abs">
  <div class="welcome-panel abs"></div>
  <div class="quick-item abs" style="top:70px"><div class="quick-bar abs">Find A Provider</div>
    <svg class="quick-icon abs" viewBox="0 0 66 66"><circle cx="33" cy="33" r="30" fill="#fff" stroke="#7d7d7f" stroke-width="3"/><circle cx="30" cy="30" r="8" fill="none" stroke="#222" stroke-width="3"/><path d="M36 36l8 8" stroke="#222" stroke-width="3"/></svg></div>
  <div class="quick-item abs" style="top:143px"><div class="quick-bar abs">Book An Appointment</div>
    <svg class="quick-icon abs" viewBox="0 0 66 66"><circle cx="33" cy="33" r="30" fill="#fff" stroke="#7d7d7f" stroke-width="3"/><rect x="21" y="22" width="24" height="22" rx="2" fill="none" stroke="#222" stroke-width="3"/><path d="M21 29h24M27 18v6M39 18v6" stroke="#222" stroke-width="3"/></svg></div>
  <div class="quick-item abs" style="top:221px"><div class="quick-bar abs">Locations</div>
    <svg class="quick-icon abs" viewBox="0 0 66 66"><circle cx="33" cy="33" r="30" fill="#fff" stroke="#7d7d7f" stroke-width="3"/><path d="M33 46s-9-10-9-17a9 9 0 0118 0c0 7-9 17-9 17z" fill="none" stroke="#222" stroke-width="3"/><circle cx="33" cy="29" r="3" fill="#222"/></svg></div>
  <div class="quick-item abs" style="top:299px"><div class="quick-bar abs">Patient Resources</div>
    <svg class="quick-icon abs" viewBox="0 0 66 66"><circle cx="33" cy="33" r="30" fill="#fff" stroke="#7d7d7f" stroke-width="3"/><circle cx="30" cy="27" r="6" fill="#222"/><path d="M19 44a11 11 0 0122 0z" fill="#222"/><path d="M42 30v10M37 35h10" stroke="#222" stroke-width="3"/></svg></div>
  <div class="quick-item abs" style="top:377px"><div class="quick-bar abs">Contact Us</div>
    <svg class="quick-icon abs" viewBox="0 0 66 66"><circle cx="33" cy="33" r="30" fill="#fff" stroke="#7d7d7f" stroke-width="3"/><rect x="21" y="24" width="24" height="17" fill="none" stroke="#222" stroke-width="3"/><path d="M21 24l12 9 12-9" fill="none" stroke="#222" stroke-width="3"/></svg></div>

  <div class="welcome-copy abs">
    <p class="eyebrow">Welcome To</p>
    <h2 class="section-title display" style="margin-top:8px">Brightway Care Clinics Services</h2>
    <p class="body-copy" style="margin-top:10px">Lorem Ipsum is simply dummy text of the printing and typesetting industry. Lorem Ipsum has been the industry's standard dummy text ever since the 1500s, when an unknown printer took a galley of type and scrambled it to make a type specimen book. It has survived not only five centuries, but also the leap into electronic typesetting, remaining essentially unchanged.</p>
    <p class="body-copy" style="margin-top:6px">It was popularised in the 1960s with the release of Letraset sheets containing Lorem Ipsum passages,</p>
  </div>
  <div class="doctors abs" role="img" aria-label="Photo of two smiling doctors in white coats holding a blue folder"></div>
</section>

<section class="services abs">
  <p class="eyebrow abs center" style="left:0;top:52px;width:1200px">our Services</p>
  <h2 class="section-title display abs center" style="left:0;top:78px;width:1200px">What We Do</h2>
  <div class="service abs center" style="left:67px;top:149px">
    <div class="service-photo" role="img" aria-label="Photo of a doctor checking a child held by her mother" style="background:linear-gradient(135deg,#e9eef2,#6b8fb0)"></div>
    <h3>family Medicine</h3>
    <p>Lorem Ipsum is simply dummy text of the printing and typesetting industry. Lorem Ipsum has been the industry's</p>
  </div>
  <div class="service abs center" style="left:429px;top:149px">
    <div class="service-photo feature" role="img" aria-label="Photo of two women in white coats reviewing a tablet" style="background:linear-gradient(135deg,#f3f3f3,#b9b4ae)"></div>
    <h3 style="color:var(--teal)">Women's health</h3>
    <p>Lorem Ipsum is simply dummy text of the printing and typesetting industry. Lorem Ipsum has been the industry's</p>
  </div>
  <div class="service abs center" style="left:793px;top:149px">
    <div class="service-photo" role="img" aria-label="Photo of a doctor comforting a worried young patient" style="background:linear-gradient(135deg,#ece6e2,#c4b3a8)"></div>
    <h3>Mental health</h3>
    <p>Lorem Ipsum is simply dummy text of the printing and typesetting industry. Lorem Ipsum has been the industry's</p>
  </div>
</section>

<section class="testimonials abs">
  <p class="eyebrow abs center" style="left:0;top:82px;width:1200px">Testimonials</p>
  <h2 class="section-title display abs center" style="left:0;top:108px;width:1200px">What Our Patient Are Says...</h2>
  <svg class="abs" style="left:184px;top:198px" width="50" height="50" viewBox="0 0 50 50"><rect x="10" y="10" width="30" height="30" rx="6" transform="rotate(45 25 25)" fill="none" stroke="#33c6d3" stroke-width="2"/><path d="M34 25H16M22 19l-6 6 6 6" fill="none" stroke="#222" stroke-width="2"/></svg>
  <svg class="abs" style="left:956px;top:198px" width="50" height="50" viewBox="0 0 50 50"><rect x="10" y="10" width="30" height="30" rx="6" transform="rotate(45 25 25)" fill="none" stroke="#7d7d7f" stroke-width="2"/><path d="M16 25h18M28 19l6 6-6 6" fill="none" stroke="#222" stroke-width="2"/></svg>
  <p class="quote abs center">One of the worst clinics I've ever seen in my life. You need to do something and change your staff and all the girls working in the reception without any exceptions. Either they hang up on you or transfer your call before you even finish what you're saying, or never call you back. I can't express how I feel about this right now! I've been trying to get an appointment for my baby for more than a week now and the person that is supposed to call me back never does! And when I call today for the million time, guess what? The internet and we will call you back! What is the purpose of having a family doctor if you always go to a walk-in clinic???</p>
  <p class="author display abs center" style="left:0;top:345px;width:1200px">Lena Morrow</p>
</section>

<section class="news abs">
  <p class="eyebrow abs center" style="left:0;top:50px;width:1200px">Keep Updated</p>
  <h2 class="section-title display abs center" style="left:0;top:78px;width:1200px">news and upcoming events</h2>

  <article class="news-card abs" style="left:60px">
    <div class="news-photo" role="img" aria-label="Photo of a doctor consulting a patient across a desk" style="background:linear-gradient(120deg,#eef0f2,#c9c6cf)"></div>
    <div class="news-meta abs"><span>▦</span><span>5 Oct 2022</span><span style="opacity:.5">|</span><span>●</span><span>Admin</span></div>
    <h4>Lorem Ipsum is simply dummy text of the printing</h4>
    <p>Lorem Ipsum is simply dummy text of the printing and typesetting industry.</p>
    <a class="learn">Learn More <svg width="24" height="10" viewBox="0 0 24 10"><path d="M0 5h22M17 1l5 4-5 4" fill="none" stroke="#33c6d3" stroke-width="1.6"/></svg></a>
  </article>
  <article class="news-card abs" style="left:430px">
    <div class="news-photo" role="img" aria-label="Photo of two nurses looking at a tablet in a hospital corridor" style="background:linear-gradient(120deg,#d9e7ef,#3f8fc2)"></div>
    <div class="news-meta abs"><span>▦</span><span>5 Oct 2022</span><span style="opacity:.5">|</span><span>●</span><span>Admin</span></div>
    <h4>Lorem Ipsum is simply dummy text of the printing</h4>
    <p>Lorem Ipsum is simply dummy text of the printing and typesetting industry.</p>
    <a class="learn">Learn More <svg width="24" height="10" viewBox="0 0 24 10"><path d="M0 5h22M17 1l5 4-5 4" fill="none" stroke="#33c6d3" stroke-width="1.6"/></svg></a>
  </article>
  <article class="news-card abs" style="left:800px">
    <div class="news-photo" role="img" aria-label="Photo of a mother and child high-fiving a doctor in an exam room" style="background:linear-gradient(120deg,#c7d3dc,#e9e0d6)"></div>
    <div class="news-meta abs"><span>▦</span><span>5 Oct 2022</span><span style="opacity:.5">|</span><span>●</span><span>Admin</span></div>
    <h4>Lorem Ipsum is simply dummy text of the printing</h4>
    <p>Lorem Ipsum is simply dummy text of the printing and typesetting industry.</p>
    <a class="learn">Learn More <svg width="24" height="10" viewBox="0 0 24 10"><path d="M0 5h22M17 1l5 4-5 4" fill="none" stroke="#33c6d3" stroke-width="1.6"/></svg></a>
  </article>
</section>

<section class="cta abs" role="img" aria-label="Teal-tinted background photo of a doctor with a stethoscope">
  <p class="eyebrow abs center" style="left:0;top:62px;width:1140px">Find A Doctor</p>
  <h2 class="cta-title display abs center" style="left:0;top:96px;width:1140px">Get Free In Schedule in An<br>Appointment Today</h2>
  <p class="body-copy abs center" style="left:285px;top:196px;width:570px;color:#fff">Lorem Ipsum is simply dummy text of the printing and typesetting industry. Lorem Ipsum has been the industry's standard dummy text.</p>
  <a class="cta-btn abs center" style="left:460px;top:278px;width:196px;height:36px;line-height:36px">Book An Appointment</a>
</section>

<footer class="site-footer abs">
  <div class="brand abs" style="left:60px;top:80px">
    <span class="brand-mark" style="width:40px;height:40px"></span>
    <span class="brand-name" style="font-size:30px">brightway</span>
  </div>
  <p class="abs" style="left:60px;top:160px;width:240px;font-size:12px;line-height:19px">Renovations have begun at our Riverside location! Over the next several months, we will be renovating the entire clinic.</p>

  <p class="foot-head abs" style="left:339px;top:71px">Quick Links</p>
  <ul class="foot-list abs" style="left:339px;top:116px">
    <li>Locations</li><li>For Patients</li><li>For Providers</li><li>About Us</li><li>Book Online</li><li>Contact Us</li>
  </ul>

  <p class="foot-head abs" style="left:615px;top:71px">Contact Us</p>
  <p class="abs" style="left:615px;top:120px;font-size:12.5px;display:flex;gap:10px;align-items:center">
    <svg width="16" height="16" viewBox="0 0 24 24"><path fill="none" stroke="#33c6d3" stroke-width="2" d="M6.6 10.8a15 15 0 006.6 6.6l2.2-2.2a1 1 0 011-.25 11.4 11.4 0 003.6.57 1 1 0 011 1V20a1 1 0 01-1 1A17 17 0 013 4a1 1 0 011-1h3.5a1 1 0 011 1 11.4 11.4 0 00.57 3.6 1 1 0 01-.25 1z"/></svg>+1 604-555-0148</p>
  <p class="abs" style="left:615px;top:160px;font-size:12.5px;display:flex;gap:10px;align-items:center">
    <svg width="18" height="14" viewBox="0 0 18 14"><rect x="1" y="1" width="16" height="12" fill="none" stroke="#33c6d3" stroke-width="1.5"/><path d="M1 1l8 6 8-6" fill="none" stroke="#33c6d3" stroke-width="1.5"/></svg>hello@brightwaycareclinics.ca</p>

  <p class="foot-head abs" style="left:890px;top:71px">Connect With Us</p>
  <div class="abs" style="left:890px;top:112px;display:flex;gap:11px">
    <span class="social on"></span><span class="social"></span><span class="social"></span>
  </div>
</footer>
<div class="copyright abs">©2022 by Brightway Care Clinics. All Right Reserved.</div>

</body>
</html>
```